Premium Personal Brand — Facebook Banner (Used Across All Platforms)

Update — Additional Color Direction
In addition to the dark charcoal/slate direction already described, I'm also interested in seeing variants with:
Dark navy blue — Deep, authoritative, intelligence-community feel. Same textured/matte treatment, not flat or bright.
Warm charcoal with steel blue accent — Keep the dark base but introduce a subtle steel blue gradient, accent line, or tonal shift. Sophisticated, modern, adds dimension without adding color noise.
Both should maintain the same premium, restrained, architectural feel described in the original brief. No bright blues, no corporate PowerPoint energy — think midnight, think depth, think weight.
Everything else in the brief remains the same.
I am building a premium personal brand as an executive advisor to founders ($5M+ revenue).
This contest is Facebook-banner–focused, but the design must represent a visual system that will be reused across:
- LinkedIn
- YouTube
I- nstagram
- X (Twitter)
- Website hero sections and other brand touchpoints
Think of the Facebook banner as the primary expression of the brand — not a one-off graphic.
This project is about discovering a high-end visual style and brand feel, not decoration.
What to design
Please submit one cohesive visual system, shown primarily as:
- Facebook banner (primary focus)
The same design language should clearly translate to all platforms listed above.
Designers are responsible for using the current recommended dimensions for each platform.
Quick clarification on background direction:
Backgrounds should have depth and texture, not flat color fields. Avoid pure white, light grey, or solid black backgrounds. Think matte, architectural materials — stone, graphite, concrete, steel — not blank canvases. Subtle tonal variation is encouraged. Obvious gradients or decorative patterns are not.
Text to use
Primary Headline:
- Your Business Is Too Valuable To Be Run On Hope.
Subheadline:
- You didn’t build a business to become its prisoner.
Name:
Paul Whitaker
The headline should be the dominant visual element.
Logo note (important)
My personal logo is currently being finalized.
For this contest:
- Use a simple “PW” monogram placeholder
- Clean, bold, geometric sans-serif
- Do not design a logo
- The winning design must allow an easy logo swap later.
Headshot note (important)
- Please do not include a headshot in the banner design.
- Most platforms display a circular profile image separately.
- The banner should stand on its own using typography, layout, and tone only.
- Design the banner assuming the profile photo will sit nearby, not inside the banner.
Style direction
The design should feel:
- Premium
- Calm
- Confident
- Restrained
- High-trust
- Dark, neutral backgrounds are preferred.
- Fewer elements are better than more.
Think:
- Owner-level advisor
- Private equity / boardroom tone
- Industrial, Modern, Minimalist, Elite, Architectural, not decorative
What to avoid
Please do not submit designs that feel:
- Promotional, hype-driven, or salesy
- Like a coach, guru, or agency
- Bright, colorful, or gradient-heavy
- Busy or over-designed
- Based on stock photos
- No motivational speaker energy.
Reaction test
- If someone sees this banner on Facebook (or later on LinkedIn, YouTube, etc.), the reaction should be:
“That person is serious. I’d trust them with important decisions.”
Final note
- I am not looking for many variations.
- I am looking for one strong visual direction you believe in.
Simple beats clever.
- Restraint beats decoration.

```html
<!DOCTYPE html>
<html lang="en">
<head>
<meta charset="utf-8">
<title>Paul Whitaker — Facebook Banner</title>
<link rel="stylesheet" href="https://fonts.googleapis.com/css2?family=Barlow+Condensed:wght@500;600;700&display=swap">
<style>
  :root {
    --slate-deep: #1c1c1c;
    --slate-mid: #2e2e2e;
    --slate-light: #444444;
    --headline-ivory: #d9dacd;
    --headline-grey: #8d8d8b;
    --sub-ivory: #d3d4c6;
    --rule: #d8d8d0;
    --name-grey: #808080;
  }
  html, body {
    margin: 0;
    padding: 0;
    width: 1200px;
    height: 527px;
    overflow: hidden;
    background: var(--slate-deep);
  }
  .banner {
    position: relative;
    width: 1200px;
    height: 527px;
    overflow: hidden;
  }
  .banner__stone {
    position: absolute;
    inset: 0;
    width: 1200px;
    height: 527px;
  }
  .banner__type {
    position: absolute;
    inset: 0;
    width: 1200px;
    height: 527px;
  }
  .headline {
    font-family: "Barlow Condensed", "Arial Narrow", sans-serif;
    font-weight: 600;
    font-size: 112px;
    text-anchor: middle;
  }
  .headline__line { fill: var(--headline-ivory); }
  .headline__line--muted { fill: var(--headline-grey); fill-opacity: 0.85; }
  .subheadline {
    font-family: "Barlow Condensed", "Arial Narrow", sans-serif;
    font-weight: 600;
    font-size: 40px;
    fill: var(--sub-ivory);
    text-anchor: middle;
  }
  .signature {
    font-family: "Barlow Condensed", "Arial Narrow", sans-serif;
    font-weight: 600;
    font-size: 44px;
    fill: var(--name-grey);
    text-anchor: middle;
  }
  .rule { stroke: var(--rule); stroke-width: 1.2; }
</style>
</head>
<body>
  <main class="banner">
    <svg class="banner__stone" viewBox="0 0 1200 527" xmlns="http://www.w3.org/2000/svg" role="img" aria-label="Dark graphite slate stone surface with faint pale veins">
      <defs>
        <linearGradient id="stone-tone" x1="0" y1="0" x2="1" y2="1">
          <stop offset="0" stop-color="#353535"/>
          <stop offset="0.45" stop-color="#2a2a2a"/>
          <stop offset="0.75" stop-color="#303030"/>
          <stop offset="1" stop-color="#1e1e1e"/>
        </linearGradient>
        <radialGradient id="stone-glow" cx="0.35" cy="0.35" r="0.6">
          <stop offset="0" stop-color="#4a4a4a" stop-opacity="0.45"/>
          <stop offset="1" stop-color="#4a4a4a" stop-opacity="0"/>
        </radialGradient>
        <filter id="stone-grain" x="0" y="0" width="100%" height="100%">
          <feTurbulence type="fractalNoise" baseFrequency="0.9" numOctaves="2" seed="4" result="noise"/>
          <feColorMatrix type="matrix" values="0 0 0 0 0.8  0 0 0 0 0.8  0 0 0 0 0.8  0 0 0 0.22 0"/>
        </filter>
        <filter id="stone-mottle" x="0" y="0" width="100%" height="100%">
          <feTurbulence type="fractalNoise" baseFrequency="0.006 0.012" numOctaves="3" seed="9"/>
          <feColorMatrix type="matrix" values="0 0 0 0 0  0 0 0 0 0  0 0 0 0 0  0 0 0 -1.4 0.9"/>
        </filter>
      </defs>
      <rect width="1200" height="527" fill="url(#stone-tone)"/>
      <rect width="1200" height="527" fill="url(#stone-glow)"/>
      <rect width="1200" height="527" filter="url(#stone-mottle)" opacity="0.5"/>
      <rect width="1200" height="527" filter="url(#stone-grain)"/>
    </svg>
    <svg class="banner__type" viewBox="0 0 1200 527" xmlns="http://www.w3.org/2000/svg">
      <defs>
        <filter id="letter-shadow" x="-10%" y="-20%" width="120%" height="150%">
          <feDropShadow dx="0" dy="6" stdDeviation="5" flood-color="#000" flood-opacity="0.6"/>
        </filter>
      </defs>
      <g class="headline" filter="url(#letter-shadow)">
        <text class="headline__line" x="601" y="128" textLength="880" lengthAdjust="spacing">YOUR BUSINESS IS</text>
        <text class="headline__line headline__line--muted" x="603" y="216" textLength="839" lengthAdjust="spacing">TOO VALUABLE TO</text>
        <text class="headline__line" x="604" y="304" textLength="823" lengthAdjust="spacing">BE RUN ON HOPE.</text>
      </g>
      <line class="rule" x1="205" y1="340" x2="995" y2="340"/>
      <text class="subheadline" x="601" y="388" textLength="764" lengthAdjust="spacing">You didn’t build a business to become its prisoner.</text>
      <line class="rule" x1="205" y1="413" x2="978" y2="413"/>
      <text class="signature" x="600" y="478" textLength="292" lengthAdjust="spacing">PAUL WHITAKER</text>
    </svg>
  </main>
</body>
</html>
```